Intuitive, look stunning website design for the street-level digital media platform that connects audiences with dynamic media on taxis and rideshare vehicles on BACK AND SIDE WINDOWS OF THE VEHICLE. SO FOOT TRAFFIC AND ALL OTHER TRAFFIC CAN SEE DISPLAY ON MOVING VEHICLE (in the future high glass building glass concept)
There should be 7 tabs VORTELANE as home button, advertisers, partners, drivers, about us, news and contact.

Target Market(s)

The company works with taxi companies and rideshare drivers to install its proprietary advertising displays in their vehicles. These proprietary screens deliver dynamic content based on location-based, WiFi-enabled triggers.

Vortelane provides an additional revenue stream to maximize drive time and empowers brands to efficiently engage consumers across our nation's busiest cities, including San Francisco, Los Angeles, New York City, Dallas, Austin, Chicago and Miami.

Industry/Entity Type

Digital Marketing

Coding

Coded - Design and coding required

Number of Pages Required

5+ page

Font styles to use
Sans Serif

Requirements
Must have
• Use beautiful graphics and easy to read fonts.
Make sure graphics are compressed and optimized for fast loading.
Design should be consistent on brand throughout the website design.
Design an intuitive navigation system which allows users to get to the pages they need quickly.
Create pages that are standard for all business from small to big such; home, about us, product/services , sitemap ( seo purposes) contact us etc..
icons links for snapchat, instagram, client login, facbook
Nice to have
• Out of box concept
Should not have
• ITS NOT AN LCD BOX PLACED OVER THE CAR

```html
<!DOCTYPE html>
<html lang="en">
<head>
<meta charset="utf-8">
<title>Vortelane – Put your brand on the road</title>
<link rel="stylesheet" href="https://fonts.googleapis.com/css2?family=Montserrat:wght@300;400;500;600;700;800;900&family=Raleway:wght@400;500&display=swap">
<style>
:root{
  --navy:#1c4f9c;
  --blue:#1fa7df;
  --yellow:#f9d71c;
  --paper:#f5f5f5;
  --grey:#6b6b6b;
  --muted:#9a9a9a;
  --white:#ffffff;
}
*{box-sizing:border-box;margin:0;padding:0}
html,body{width:1200px;height:2761px;overflow:hidden}
body{position:relative;background:var(--paper);font-family:"Montserrat",sans-serif;color:var(--navy)}
a{text-decoration:none;color:inherit}
.backdrop{position:absolute;left:0;top:0;width:1200px;height:2761px}
.abs{position:absolute}

/* header */
.brand{left:92px;top:18px;display:flex;align-items:center;gap:12px}
.brand-dot{width:46px;height:46px;border-radius:50%;background:var(--blue)}
.brand-name{font-size:22px;font-weight:700;letter-spacing:3px;color:var(--navy)}
.main-nav{left:410px;top:11px;display:flex;gap:28px;font-size:12px;font-weight:700;color:var(--navy);white-space:nowrap}
.client-login{left:961px;top:0;width:148px;height:40px;background:var(--navy);color:var(--white);border-radius:0 0 4px 4px;font-size:12px;font-weight:700;display:flex;align-items:center;justify-content:center;gap:8px}
.client-login svg{width:20px;height:20px}
.social-top{left:983px;top:52px;display:flex;gap:24px}
.social-top span{width:18px;height:18px;border-radius:50%;background:var(--yellow);display:block}

/* hero */
.hero-title{left:92px;top:214px;font-size:38px;line-height:40px;font-weight:800;color:var(--navy);letter-spacing:-0.5px;white-space:nowrap}
.hero-sub{left:92px;top:300px;font-size:16px;font-weight:400;color:var(--blue);white-space:nowrap}
.btn-learn{left:92px;top:340px;width:181px;height:46px;border-radius:23px;background:var(--yellow);color:var(--navy);font-size:13px;font-weight:800;display:flex;align-items:center;justify-content:center}
.hero-vehicle{left:540px;top:200px;width:660px;height:430px;border-radius:160px 90px 40px 60px;background:linear-gradient(180deg,#e9e9e9 0%,#f2de1a 35%,#e3c50d 80%,#2b2b2b 100%)}

/* rules band */
.rules-title{left:96px;top:754px;font-size:34px;font-weight:800;color:var(--white);letter-spacing:-0.5px;white-space:nowrap}
.rules-sub{left:96px;top:793px;font-size:17px;color:var(--white);white-space:nowrap}
.rules-bar{left:643px;top:735px;width:7px;height:98px;background:var(--yellow);border-radius:4px}
.rules-points{left:670px;top:747px;font-size:16px;line-height:22px;color:var(--white);white-space:nowrap}

/* advantages */
.adv-title{left:0;top:1048px;width:1200px;text-align:center;font-size:34px;line-height:40px;color:var(--navy)}
.adv-title .light{font-weight:300;display:block}
.adv-title .bold{font-weight:800;display:block}
.advantage{top:1170px;width:290px;text-align:center}
.advantage svg{width:96px;height:96px;display:block;margin:0 auto}
.advantage h3{margin-top:44px;font-size:18px;font-weight:700;color:var(--navy)}
.advantage p{margin-top:12px;font-size:16px;line-height:20px;color:var(--grey)}

/* evolution */
.evo-title{left:95px;top:1676px;width:480px;text-align:center;font-size:36px;line-height:42px;color:var(--white)}
.evo-title .light{font-weight:300;display:block}
.evo-title .bold{font-weight:800;display:block}
.evo-copy{left:92px;top:1818px;width:472px;text-align:center;font-size:19px;line-height:24px;color:var(--white)}
.rear-vehicle{left:590px;top:1532px;width:610px;height:594px;border-radius:200px 0 60px 60px;background:linear-gradient(180deg,#e7d23a 0%,#d8bf1a 20%,#3a3f7a 22%,#283067 40%,#e3c520 42%,#c9ad12 90%,#2a2a2a 100%)}

/* stats */
.stat{top:2150px;width:260px;text-align:center;color:var(--white)}
.stat b{display:block;font-size:92px;line-height:96px;font-weight:900;letter-spacing:-3px}
.stat b sup{font-size:38px;vertical-align:top;line-height:60px;letter-spacing:0}
.stat span{display:block;font-size:12px;font-weight:800;letter-spacing:.3px;margin-top:2px}

/* footer */
.foot-brand{left:92px;top:2474px;display:flex;align-items:center;gap:12px}
.foot-brand .brand-dot{width:56px;height:56px}
.foot-contact{left:92px;top:2551px;font-family:"Raleway",sans-serif;font-size:14px;line-height:30.5px;color:var(--muted)}
.foot-col{top:2521px;font-family:"Raleway",sans-serif}
.foot-col h4{font-family:"Montserrat",sans-serif;font-size:14px;font-weight:600;color:var(--blue);margin-bottom:10px}
.foot-col li{list-style:none;font-size:15px;line-height:30.5px;color:var(--muted)}
.foot-social{left:925px;top:2560px;display:flex;gap:28px}
.foot-social span{width:26px;height:26px;border-radius:50%;background:var(--blue);display:block}
.legal{left:0;top:2728px;width:1200px;text-align:center;font-family:"Raleway",sans-serif;font-size:13px;color:var(--muted);word-spacing:2px}
.legal i{font-style:normal;margin:0 22px}
</style>
</head>
<body>

<svg class="backdrop" viewBox="0 0 1200 2761" preserveAspectRatio="none" aria-hidden="true">
  <path d="M0 523 C300 505 700 470 1200 300 L1200 730 C900 880 500 980 0 1025 Z" fill="#1fa7df"/>
  <path d="M0 1520 C300 1560 600 1640 750 1610 C900 1580 1050 1540 1200 1530 L1200 2510 C900 2500 400 2360 0 2195 Z" fill="#1fa7df"/>
</svg>

<header>
  <a class="abs brand" href="#home"><span class="brand-dot"></span><span class="brand-name">VORTELANE</span></a>
  <nav class="abs main-nav">
    <a href="#advertisers">ADVERTISERS</a><a href="#partners">PARTNERS</a><a href="#drivers">DRIVERS</a><a href="#about">ABOUT US</a><a href="#news">NEWS</a><a href="#contact">CONTACT</a>
  </nav>
  <a class="abs client-login" href="#login">
    <svg viewBox="0 0 20 20" fill="none" stroke="#fff" stroke-width="1.5"><circle cx="10" cy="10" r="9"/><circle cx="10" cy="8" r="3"/><path d="M4.5 16c1.5-2.5 3.5-3.5 5.5-3.5s4 1 5.5 3.5"/></svg>
    CLIENT LOGIN
  </a>
  <div class="abs social-top" aria-label="Social links"><span></span><span></span><span></span></div>
</header>

<section class="hero">
  <div class="abs hero-vehicle" role="img" aria-label="Yellow taxi seen from the side with a food advert showing on its rear side window"></div>
  <h1 class="abs hero-title">PUT YOUR BRAND ON<br>THE ROAD</h1>
  <p class="abs hero-sub">With the fastest growing transit media platform</p>
  <a class="abs btn-learn" href="#advertisers">LEARN MORE</a>
</section>

<section class="rules">
  <h2 class="abs rules-title">YOUR BRAND, YOUR RULES!</h2>
  <p class="abs rules-sub">Your scale, your budget, your advertising medium.</p>
  <span class="abs rules-bar"></span>
  <p class="abs rules-points">An agile format built around a truly agile team.<br>A bespoke and unrestricted media format.<br>A roving canvas to elevate your brand.</p>
</section>

<section class="advantages">
  <h2 class="abs adv-title"><span class="light">SOME OF THE TOP NOTCH</span><span class="bold">ADVANTAGES OF VEHICLE WRAP</span></h2>

  <div class="abs advantage" style="left:103px">
    <svg viewBox="0 0 96 96" fill="#1fa7df" stroke="#1fa7df" stroke-width="2">
      <circle cx="48" cy="48" r="9"/>
      <g stroke-linecap="round"><line x1="48" y1="36" x2="48" y2="20"/><line x1="48" y1="60" x2="48" y2="76"/><line x1="36" y1="48" x2="20" y2="48"/><line x1="60" y1="48" x2="76" y2="48"/><line x1="40" y1="40" x2="28" y2="28"/><line x1="56" y1="56" x2="68" y2="68"/><line x1="56" y1="40" x2="68" y2="28"/><line x1="40" y1="56" x2="28" y2="68"/></g>
      <circle cx="48" cy="12" r="5"/><circle cx="48" cy="84" r="5"/><circle cx="12" cy="48" r="5"/><circle cx="84" cy="48" r="5"/><circle cx="22" cy="22" r="4"/><circle cx="74" cy="74" r="4"/><circle cx="74" cy="22" r="4"/><circle cx="22" cy="74" r="4"/>
    </svg>
    <h3>REACH &amp; DATA</h3>
    <p>The world has begun to see the vehicle exterior and top as an under utilized advertising medium in desperate need of disruption. In both the traditional taxi and ride-sharing spaces.</p>
  </div>

  <div class="abs advantage" style="left:447px">
    <svg viewBox="0 0 96 96" fill="none" stroke="#1fa7df" stroke-width="2.5" stroke-linejoin="round">
      <path d="M88 8 C60 10 42 26 32 48 L48 64 C70 54 86 36 88 8 Z"/>
      <circle cx="64" cy="32" r="8" fill="#1fa7df"/>
      <path d="M32 48 L18 46 L28 34 L40 34"/><path d="M48 64 L50 78 L62 68 L62 56"/>
      <path d="M28 60 L10 86 M34 66 L18 88 M24 56 L8 74"/>
    </svg>
    <h3>EXTENSIVE REACH</h3>
    <p>The world has begun to see the vehicle exterior and top as an under utilized advertising medium in desperate need of disruption. In both the traditional taxi and ride-sharing spaces.</p>
  </div>

  <div class="abs advantage" style="left:783px">
    <svg viewBox="0 0 96 96" fill="none" stroke="#1fa7df" stroke-width="3" stroke-linecap="round">
      <path d="M6 48 C24 24 72 24 90 48 C72 72 24 72 6 48 Z" fill="#fff"/>
      <circle cx="48" cy="48" r="14" fill="#1fa7df"/><circle cx="53" cy="43" r="5" fill="#fff" stroke="none"/>
      <line x1="48" y1="4" x2="48" y2="16"/><line x1="48" y1="80" x2="48" y2="92"/><line x1="24" y1="12" x2="30" y2="22"/><line x1="72" y1="12" x2="66" y2="22"/><line x1="24" y1="84" x2="30" y2="74"/><line x1="72" y1="84" x2="66" y2="74"/>
    </svg>
    <h3>APPEALING TO THE EYES</h3>
    <p>The world has begun to see the vehicle exterior and top as an under utilized advertising medium in desperate need of disruption. In both the traditional taxi and ride-sharing spaces.</p>
  </div>
</section>

<section class="evolution">
  <h2 class="abs evo-title"><span class="light">THE NEXT EVOLUTION OF</span><span class="bold">DIGITAL OUTDOOR ADVERTISING</span></h2>
  <p class="abs evo-copy">The world has begun to see the vehicle exterior and top as an under utilized advertising medium in desperate need of disruption. In both the traditional taxi and ride-sharing spaces.</p>
  <div class="abs rear-vehicle" role="img" aria-label="Yellow taxi seen from behind with a live sports advert playing on its rear window"></div>
</section>

<section class="stats">
  <div class="abs stat" style="left:172px"><b>1B<sup>+</sup></b><span>MONTHLY IMPRESSIONS</span></div>
  <div class="abs stat" style="left:478px"><b>35K<sup>+</sup></b><span>DISPLAYS</span></div>
  <div class="abs stat" style="left:771px"><b>20<sup>+</sup></b><span>KEY MARKETS</span></div>
</section>

<footer>
  <a class="abs foot-brand" href="#home"><span class="brand-dot"></span><span class="brand-name">VORTELANE</span></a>
  <address class="abs foot-contact" style="font-style:normal">14 Harlow Yard, EC2 4PL<br>London, United Kingdom<br>info@vortelane.com<br>+44 (0) 200 000 4182</address>
  <div class="abs foot-col" style="left:390px"><h4>SERVICE</h4><ul><li>Drive</li><li>Advertise</li><li>Wrap for us</li><li>Franchise</li></ul></div>
  <div class="abs foot-col" style="left:573px"><h4>QUICKLINKS</h4><ul><li>Drive</li><li>Advertise</li><li>Wrap for us</li><li>Franchise</li></ul></div>
  <div class="abs foot-col" style="left:747px"><h4>COMPANY</h4><ul><li>About</li><li>Careers</li><li>Blog</li><li>FAQ</li></ul></div>
  <div class="abs foot-col" style="left:925px"><h4>FOLLOW US</h4></div>
  <div class="abs foot-social" aria-label="Social links"><span></span><span></span><span></span></div>
  <p class="abs legal">© Vortelane 2020<i>|</i>Privacy And Cookies Policy<i>|</i>Terms of Use</p>
</footer>

</body>
</html>
```